FRONT BUS CARD:

We were maybe thinking to have the text in a "common seal" which is an oval shape. Or CROWN VAULT underlined, then AUSTRALIA underneath...

Picture to have in the seal, or next to the words if seal not used: Gold Bars (3 of them), or scales of justice..

LOGO and pic and font to be in shiny gold.
We want 1 black background design and 1 white background design.

CROWN VAULT TRADERS

```html
<!DOCTYPE html>
<html lang="en">
<head>
<meta charset="utf-8">
<title>Crown Vault Traders – Business Cards</title>
<link rel="stylesheet" href="https://fonts.googleapis.com/css2?family=Roboto+Condensed:wght@700&family=Arimo:wght@400;700&display=swap">
<style>
  :root {
    --backdrop: #e9e6e1;
    --card-black: #141414;
    --card-edge: #262626;
    --gold: #c9a24a;
    --gold-light: #e6c46e;
    --gold-deep: #8a6420;
  }
  * { box-sizing: border-box; margin: 0; padding: 0; }
  html, body {
    width: 1200px; height: 800px; overflow: hidden;
    background: var(--backdrop);
  }
  .canvas {
    position: relative; width: 1200px; height: 800px;
    display: flex; align-items: center; justify-content: center; gap: 50px;
  }
  .card {
    position: relative; width: 530px; height: 300px;
    background: var(--card-black);
    border: 1px solid var(--card-edge);
    border-radius: 18px;
    box-shadow: 0 10px 26px rgba(0,0,0,.28);
    overflow: hidden;
  }
  .brand-name {
    font-family: "Roboto Condensed", "Arial Narrow", sans-serif;
    font-weight: 700; color: var(--gold);
    text-transform: uppercase; line-height: 1;
  }
  .mark-circle {
    position: absolute; border-radius: 50%;
    background: radial-gradient(circle at 35% 30%, var(--gold-light), var(--gold) 55%, var(--gold-deep));
  }

  /* Front */
  .card-front .mark-circle { width: 96px; height: 96px; left: 217px; top: 48px; }
  .card-front .brand-block {
    position: absolute; left: 0; right: 0; top: 166px; text-align: center;
  }
  .card-front .brand-name-main { font-size: 52px; letter-spacing: .5px; }
  .card-front .brand-name-sub {
    font-size: 24px; text-align: right; padding-right: 62px; margin-top: 2px;
  }

  /* Back */
  .card-back .mark-circle { width: 130px; height: 130px; left: 48px; top: 85px; }
  .card-back .details { position: absolute; left: 262px; top: 92px; }
  .card-back .brand-name-main { font-size: 24px; }
  .card-back .brand-name-sub { font-size: 12px; text-align: right; width: 152px; margin-bottom: 10px; }
  .contact-list { list-style: none; font-family: "Arimo", Arial, sans-serif; font-size: 13px; color: var(--gold-light); }
  .contact-list li { margin-bottom: 5px; white-space: nowrap; }
  .contact-label { font-weight: 700; }
</style>
</head>
<body>
<main class="canvas">
  <section class="card card-front" aria-label="Business card front">
    <span class="mark-circle"></span>
    <div class="brand-block">
      <div class="brand-name brand-name-main">Crown Vault</div>
      <div class="brand-name brand-name-sub">Traders</div>
    </div>
  </section>

  <section class="card card-back" aria-label="Business card back">
    <span class="mark-circle"></span>
    <div class="details">
      <div class="brand-name brand-name-main">Crown Vault</div>
      <div class="brand-name brand-name-sub">Traders</div>
      <ul class="contact-list">
        <li><span class="contact-label">Web:</span> www.crownvault.example</li>
        <li><span class="contact-label">Phone:</span> 55501234</li>
        <li><span class="contact-label">E-mail:</span> mail@crownvault.example</li>
        <li><span class="contact-label">Address:</span> Street, City, Country</li>
      </ul>
    </div>
  </section>
</main>
</body>
</html>
```